Task Description:
I’m wanting a professionally designed 8 ½' x 11, 3 fold brochure, both sides, to print as my target audience are those people who primarily don’t have access to the internet. These items will be dropped off in the mailboxes of all households in the city.
However I do have a web site www.brightcivicpath.ca where I would like to have it as a document that can be down loaded.
This is my first foray into political office and my message needs to be clear, concise and easy to understand. The brochure should be a bit conservative yet be warm and inviting. I’ve selected two pictures that I think make sense under their respective headings, but I'm open to suggestions.I need to update my picture for the front cover.
There is the possibility of having T shirts and business cards made up, which would be in essence a simpler version of the brochure so please keep this in mind. I ask that you work with me and I will compensate you accordingly for the extras should they be required. You may want to consider making the Bright Civic Path into a logo as we own all the web extensions and have applied for copyright protection for branding purposes.
You may want to look at QM Larchfield http://www.qmlarchfield.ca/ , or the Pinecrest Bank of Canada www.pinecrestbank.com as two recognizable colour schemes here in Canada but don’t let that limit your imagination.
The content in the flier should remain intact although I am open to some minor suggestions. As you can see my talents as a graphic artist are limited hence my need for that professional make over that will give it a bit of razzle dazzle and set me out from the other candidates. So use your imagination!!
Target Market(s)
Middle age voters who may or may not have access to the internet and still prefer print
Industry/Entity Type
Conservative

```html
<!DOCTYPE html>
<html lang="en">
<head>
<meta charset="utf-8">
<title>Dale Merrow – Bright Civic Path</title>
<link href="https://fonts.googleapis.com/css2?family=Arimo:ital,wght@0,400;0,700;1,700&family=Roboto+Condensed:wght@700&display=swap" rel="stylesheet">
<style>
:root{
  --blue:#0d4f9e;
  --blue-deep:#0a3f86;
  --blue-mid:#3f7cc4;
  --green:#5aac1e;
  --panel:#eef2f1;
  --white:#ffffff;
}
*{margin:0;padding:0;box-sizing:border-box}
html,body{width:1200px;height:933px;overflow:hidden;background:var(--white)}
body{font-family:"Arimo",Arial,sans-serif;position:relative}
.top-band{position:absolute;left:0;top:0;width:1200px;height:24px;background:var(--green)}
.panel{position:absolute;top:24px;height:909px}
.panel-left{left:0;width:403px;background:var(--white)}
.panel-middle{left:403px;width:392px;background:var(--panel)}
.panel-right{left:795px;width:405px;background:var(--panel)}

.name-header{position:absolute;left:0;top:0;width:403px;height:129px;background:var(--blue);color:var(--white);font-size:31px;font-weight:400;text-align:center;padding-top:42px}
.fold-rule{position:absolute;left:14px;top:135px;height:755px;border-left:2px dashed var(--blue-mid)}
.fold-rule::after{content:"";position:absolute;left:-2px;bottom:0;width:40px;border-top:2px dashed var(--blue-mid)}
.portrait{position:absolute;left:263px;top:132px;width:111px;height:153px;background:linear-gradient(160deg,#9aa3a8,#3c3f44);box-shadow:6px 6px 0 #c9d6e6}
.intro{position:absolute;left:32px;top:162px;width:225px;color:var(--blue);font-size:17px;line-height:22px}
.family{position:absolute;left:32px;top:303px;width:360px;list-style:none;color:var(--blue);font-size:17px;line-height:21.5px}
.family li{position:relative;margin-bottom:21px}
.family li::before{content:"";position:absolute;left:-7px;top:8px;width:5px;height:5px;border-radius:50%;background:var(--green)}
.bio{position:absolute;left:32px;top:564px;width:355px;color:var(--blue);font-size:17px;line-height:21.5px}
.bio p{margin-bottom:21px}
.site{position:absolute;font-weight:700;font-size:16px;letter-spacing:4px}
.panel-left .site{left:32px;top:862px;color:var(--blue)}

.involved{position:absolute;left:32px;top:50px;font-size:31px;line-height:29px;font-weight:700}
.involved .a{color:var(--blue)}
.involved .b{color:var(--green);padding-left:40px}
.involved-text{position:absolute;left:32px;top:128px;width:318px;color:var(--green);font-size:16px;line-height:21.3px}
.bus-photo{position:absolute;left:0;top:307px;width:392px;height:232px;background:linear-gradient(180deg,#6fa6de 0%,#b9d5ee 45%,#d9dde0 60%,#8b8f8f 100%)}
.goals{position:absolute;left:32px;top:566px;width:332px;color:var(--green);font-size:16px;line-height:21.3px}
.vote{position:absolute;left:32px;top:772px;font-family:"Roboto Condensed","Arial Narrow",sans-serif;font-weight:700;font-size:42px;line-height:44px}
.vote .date{color:var(--green)}
.vote .who{color:var(--blue);padding-left:38px}

.headline{position:absolute;left:92px;top:56px;color:var(--blue);font-weight:700}
.headline .unlock{display:block;font-size:50px;letter-spacing:5px;line-height:50px}
.headline .the{display:block;color:var(--green);font-size:24px;line-height:24px}
.headline .potential{display:block;font-size:50px;line-height:52px;letter-spacing:1px}
.tagline{position:absolute;left:17px;top:190px;color:var(--blue);font-weight:700;font-size:18.5px}
.cover-photo{position:absolute;left:0;top:307px;width:405px;height:263px;background:linear-gradient(135deg,#c5d7ec 0%,#8fb1d9 50%,#4f82c0 100%)}
.cover-rule{position:absolute;left:0;top:632px;width:405px;height:11px;background:var(--green)}
.cover-block{position:absolute;left:0;top:643px;width:405px;height:266px;background:linear-gradient(180deg,#3f7cc4 0%,var(--blue) 55%,var(--blue-deep) 100%);color:var(--white)}
.cover-name{position:absolute;left:95px;top:44px;font-size:40px;font-weight:700;letter-spacing:2px;line-height:46px}
.cover-sub{position:absolute;left:95px;top:94px;font-size:38px;font-weight:700;line-height:42px;letter-spacing:2px}
.cover-sub em{display:block;font-style:italic;letter-spacing:1px}
.cover-sub span{display:block;padding-left:4px}
.cover-block .site{left:84px;top:215px;color:var(--white);font-size:15px;letter-spacing:4.5px}
</style>
</head>
<body>
<div class="top-band"></div>

<section class="panel panel-left">
  <h2 class="name-header">Bright Civic Path</h2>
  <div class="fold-rule"></div>
  <div class="portrait" role="img" aria-label="Portrait photograph of the candidate"></div>
  <p class="intro">Dale Merrow is a life long resident of Birch Harbour. My family has served this community and area for more than 100 years.</p>
  <ul class="family">
    <li>Walter Henry Merrow built and managed the Harbourline Elevator.</li>
    <li>Frank Davidson Merrow managed the Greystone Cement facility</li>
    <li>Ruth Long Merrow was past president of the Chamber of Commerce.</li>
    <li>Claire Merrow is a gold medalist at the 2010 Nordic Ski Championship.</li>
  </ul>
  <div class="bio">
    <p>Although I have a unique vocation through the Process Assurance Board (PAB) and could live and work anywhere in the world I have chosen to remain and work from Birch Harbour.</p>
    <p>On average I visit and work with more than 30 different corporations a year. I have a high pressure job as companies rely on my skills and expertise to keep them safe and operational. Solving problems, minimizing costs, maximizing production are challenges I face everyday.</p>
  </div>
  <div class="site">www.brightcivicpath.ca</div>
</section>

<section class="panel panel-middle">
  <h2 class="involved"><span class="a">I’m currently</span><br><span class="b">involved with</span></h2>
  <p class="involved-text">Voltaris Labs Inc. a newly created R&amp;D company developing electric propulsion systems for the transit industry. Our research partners consist of faculty and students from Northshore College. So I know first hand how difficult it is to start, finance and run a new business in this city.</p>
  <div class="bus-photo" role="img" aria-label="Photograph of a hybrid electric city bus parked outdoors"></div>
  <p class="goals">As Bright Civic Path, my goal is to be mayor for two terms, maximum three. With the implementation of a long term plan we will require a fresh face to step forward to complete the process. I also feel that we should reduce the number of city councilors and use those funds to make those positions full time. Term limits should apply to all elected positions!</p>
  <div class="vote"><div class="date">On Oct 25th</div><div class="who">Vote Dale Merrow</div></div>
</section>

<section class="panel panel-right">
  <h1 class="headline"><span class="unlock">Unlock</span><span class="the">the</span><span class="potential">Potential</span></h1>
  <p class="tagline">Of The Best Small City In North America</p>
  <div class="cover-photo" role="img" aria-label="Cover artwork with the candidate portrait and the themes community, growth and new in blue tones"></div>
  <div class="cover-rule"></div>
  <div class="cover-block">
    <div class="cover-name">Dale Merrow</div>
    <div class="cover-sub"><em>Bright</em><span>Civic Path</span></div>
    <div class="site">www.brightcivicpath.ca</div>
  </div>
</section>
</body>
</html>
```